Urine collection cup with and without sterile seal sticker

Hello. We need a urine cup label designed please with

Name:
Date of Birth:
Date:
Time:
Temp℃:
Specimen ID:

Product code: TUB-47
Volume markings (e.g., 30 mL, 60 mL, 90 mL).
Vela Drug Tests logo

Could you please provide one version with the additional sterile sticker extending to the top, and one version without the additional sterile sticker?

```html
<!DOCTYPE html>
<html lang="en">
<head>
<meta charset="utf-8">
<title>Urine Collection Cup Label</title>
<link href="https://fonts.googleapis.com/css2?family=Bebas+Neue&display=swap" rel="stylesheet">
<style>
  :root {
    --label-yellow: #f2d511;
    --ink-black: #000000;
    --brand-blue: #4f9fd6;
    --field-white: #ffffff;
  }
  html, body {
    margin: 0;
    padding: 0;
    width: 988px;
    height: 1200px;
    overflow: hidden;
    background: var(--field-white);
  }
  .label {
    position: relative;
    width: 984px;
    height: 1196px;
    margin: 2px;
    background: var(--label-yellow);
    font-family: "Bebas Neue", "Oswald", sans-serif;
    color: var(--brand-blue);
  }
  .title-band {
    position: absolute;
    left: 98px;
    top: 93px;
    width: 789px;
    height: 162px;
    background: var(--ink-black);
    display: flex;
    align-items: center;
    justify-content: center;
  }
  .title {
    margin: 0;
    font-weight: 400;
    font-size: 96px;
    line-height: 1;
    padding-top: 10px;
    white-space: nowrap;
  }
  .field {
    position: absolute;
    left: 98px;
    width: 789px;
    height: 76px;
    box-sizing: border-box;
    border: 11px solid var(--ink-black);
    display: flex;
  }
  .field-name {
    width: 330px;
    height: 100%;
    background: var(--label-yellow);
    display: flex;
    align-items: center;
    padding-left: 28px;
    box-sizing: border-box;
    font-size: 62px;
    line-height: 1;
    padding-top: 8px;
    white-space: nowrap;
  }
  .field-entry {
    flex: 1;
    height: 100%;
    background: var(--field-white);
  }
  .product-band {
    position: absolute;
    left: 98px;
    top: 942px;
    width: 789px;
    height: 162px;
    background: var(--ink-black);
  }
  .product-code {
    position: absolute;
    left: 27px;
    top: 14px;
    font-size: 60px;
    line-height: 1;
  }
  .rule {
    position: absolute;
    top: 80px;
    height: 3px;
    background: var(--brand-blue);
  }
  .rule-left { left: 26px; width: 265px; }
  .rule-right { left: 500px; width: 265px; }
  .brand {
    position: absolute;
    left: 300px;
    top: 58px;
    width: 192px;
    display: flex;
    align-items: center;
    gap: 8px;
  }
  .brand-dot {
    flex: none;
    width: 44px;
    height: 44px;
    border-radius: 50%;
    background: var(--brand-blue);
  }
  .brand-name {
    font-size: 27px;
    line-height: 1;
    padding-top: 4px;
    white-space: nowrap;
  }
  .volume {
    position: absolute;
    right: 24px;
    top: 92px;
    font-size: 60px;
    line-height: 1;
  }
</style>
</head>
<body>
  <div class="label">
    <header class="title-band">
      <h1 class="title">URINE COLLECTION CUP</h1>
    </header>

    <div class="field" style="top:301px"><div class="field-name">NAME</div><div class="field-entry"></div></div>
    <div class="field" style="top:405px"><div class="field-name">DATE OF BIRTH</div><div class="field-entry"></div></div>
    <div class="field" style="top:508px"><div class="field-name">DATE</div><div class="field-entry"></div></div>
    <div class="field" style="top:611px"><div class="field-name">TIME</div><div class="field-entry"></div></div>
    <div class="field" style="top:715px"><div class="field-name">TEMP °C</div><div class="field-entry"></div></div>
    <div class="field" style="top:818px"><div class="field-name">SPECIMEN ID</div><div class="field-entry"></div></div>

    <footer class="product-band">
      <div class="product-code">TUB-47</div>
      <div class="rule rule-left"></div>
      <div class="brand">
        <span class="brand-dot"></span>
        <span class="brand-name">VELA DRUG TESTS</span>
      </div>
      <div class="rule rule-right"></div>
      <div class="volume">90 ML</div>
    </footer>
  </div>
</body>
</html>
```